Looking for Landingpage / Website Designer

We are looking for a Web Designer / Developer for our upcoming Start Up Websites. The first project will be a simple responsive business website with a CTA- Button and an optional Newsletter Opt-In. We do aim for a modern online business approach, since we are a young company.

It is necessary to understand, that we need a conversion orientated design, not a wordpress blog with widgets and galleries.

We are currently discussing how it is going to happen and what preferences we need to focus on.

What we know is, that it should be more of a landing page with an option of adding 2 or 3 Navigation points.

We even thought about using services like pagemarlo.com or formvista.com to have an easier approach for future customizations and A/B testing.

We'd love to see how you fit the design/colors to the upcoming logo
(which is not the final version yet )

hope you can do something about that.

For the Structure.

1. Bracket

Slogan plus a preview text of what we are offering. On the right side a video placeholder plus CTA button.

2. Bracket

Illustrating 3 Benefits. On the right side - Opt in for Contact/Newsletter and CTA Button

3. Bracket

Picture with text just like you have it with the testimonial

You can orientate yourself towards to that landing page example as well:

http://cdn2.quentarix.net/hub/53/file-581676469-png/Blog-Related_Images/pagemarlo_landing_page.png?t=1416543075530

If our collaboration is going well, we would like to stay in touch for further projects.

Reason: There are 3 Design we do really like but, don't fit exactly our needs. 5 Days max.

Reason: For final adjustments.

I just uploaded the final logo :) Thank you for your commitment so far!

Target Market(s)

Our targeted audience could be almost everybody, who looks for an average paid side job (students, unemployed, house wives and whatever you can imagine). Maybe this is enough information for you to get a mere perception of what this is all about.

Industry/Entity Type

Business

Coding

Coded - Design and coding required

Font styles to use
Serif
Sans Serif

Colors
acd037
5c5c5c
33a6d7

Requirements
Must have
• Registration Opt-In
Responsive on any Device
Customizable
A benefits navigation just like in that example I've uploaded.
Nice to have
• As fast as possible ;D

```html
<!DOCTYPE html>
<html lang="en">
<head>
<meta charset="utf-8">
<title>Workvana – Side Jobs</title>
<link href="https://fonts.googleapis.com/css2?family=Open+Sans:wght@400;600;700;800&family=Arimo:wght@400;700&family=Dancing+Script:wght@500&display=swap" rel="stylesheet">
<style>
:root{
  --green:#acd037;
  --green-dark:#9cc22b;
  --grey:#5c5c5c;
  --blue:#33a6d7;
  --blue-dark:#2288c0;
  --light:#f1f1f1;
  --text:#8a8a8a;
  --footer:#444444;
  --line:#e2e2e2;
}
*{margin:0;padding:0;box-sizing:border-box}
html,body{width:894px;height:1200px;overflow:hidden}
body{font-family:'Arimo',Arial,sans-serif;color:var(--grey);background:#fff;position:relative}
.abs{position:absolute}

/* header */
.top-line{left:0;top:0;width:894px;height:2px;background:var(--green)}
.header{left:0;top:2px;width:894px;height:92px;background:#fff}
.brand{left:97px;top:30px;display:flex;align-items:center;gap:8px}
.brand-dot{width:32px;height:32px;border-radius:50%;background:var(--green)}
.brand-name{font-family:'Open Sans',sans-serif;font-weight:700;font-size:29px;color:var(--grey);letter-spacing:-1px}
.nav{left:428px;top:2px;height:92px;display:flex;font-size:12px;color:var(--grey)}
.nav a{display:flex;align-items:center;justify-content:center;height:92px;text-decoration:none;color:inherit}
.nav .home{width:78px;background:var(--green);color:#fff;position:relative}
.nav .home::after{content:"";position:absolute;bottom:0;left:33px;border:6px solid transparent;border-bottom-color:#fff}
.nav .about{width:97px}
.nav .services{width:102px}
.nav .contact{width:108px}

/* hero */
.hero{left:0;top:94px;width:894px;height:334px;background:linear-gradient(135deg,#a6cb30,#b3d544 50%,#a3c82d)}
.hero-title{left:121px;top:148px;font-family:'Open Sans',sans-serif;font-weight:800;font-size:50px;color:#fff}
.hero-text{left:121px;top:224px;width:310px;font-size:9px;line-height:20px;color:#fff}
.cta{left:122px;top:318px;width:153px;height:36px;background:linear-gradient(#45b4e2,var(--blue-dark));border-radius:3px;color:#fff;font-family:'Open Sans',sans-serif;font-weight:700;font-size:13.5px;display:flex;align-items:center;justify-content:center;box-shadow:0 1px 2px rgba(0,0,0,.25)}
.video{left:430px;top:154px;width:367px;height:206px}

/* benefits */
.benefits{left:0;top:428px;width:894px;height:351px;background:var(--light)}
.section-title{font-family:'Open Sans',sans-serif;font-weight:700;font-size:15.5px;color:var(--green)}
.section-title span{color:var(--blue)}
.benefits-title{left:98px;top:459px}
.benefits-text{left:98px;top:490px;width:432px;font-size:8px;line-height:17px;color:var(--text)}
.benefit{top:592px;width:140px;text-align:center}
.benefit-icon{display:block;margin:0 auto;width:44px;height:42px}
.benefit h3{margin-top:12px;font-size:8.5px;font-weight:700;color:var(--grey);letter-spacing:.2px}
.benefit p{margin-top:9px;font-size:8px;line-height:14.5px;color:var(--text)}
.benefit .more{margin-top:9px;font-size:8.5px;color:var(--blue);font-weight:700}
.b1{left:93px}.b2{left:246px}.b3{left:398px}

.newsletter{left:548px;top:462px;width:248px;height:293px;background:#fff;box-shadow:0 0 4px rgba(0,0,0,.12)}
.newsletter h2{position:absolute;left:0;top:18px;width:100%;text-align:center;font-family:'Open Sans',sans-serif;font-weight:600;font-size:15.5px;color:var(--grey)}
.field{position:absolute;left:18px;width:212px;height:28px;border:1px solid var(--line);font-size:8px;color:#aaa;padding:9px 9px}
.f1{top:56px}.f2{top:93px}.f3{top:129px}.f4{top:166px;height:56px}
.submit{position:absolute;left:48px;top:238px;width:152px;height:36px;background:linear-gradient(#45b4e2,var(--blue-dark));border-radius:3px;color:#fff;font-family:'Open Sans',sans-serif;font-weight:700;font-size:13.5px;display:flex;align-items:center;justify-content:center}

/* testimonials */
.testimonials{left:0;top:779px;width:894px;height:258px;background:#f8f8f8}
.testi-title{left:100px;top:800px}
.quote{top:853px;width:220px;height:70px;background:#fff;border:1px solid #ececec;font-size:8px;line-height:17.5px;color:var(--text);padding:10px 8px 0 14px}
.quote::before{content:"\201C";position:absolute;left:4px;top:-6px;font-size:18px;color:#999;font-family:Georgia,serif}
.quote::after{content:"";position:absolute;left:18px;bottom:-7px;width:12px;height:12px;background:#fff;border-right:1px solid #ececec;border-bottom:1px solid #ececec;transform:rotate(45deg)}
.quote .close{font-family:Georgia,serif;font-size:14px;color:#999;margin-left:6px;vertical-align:-5px}
.q1{left:98px}.q2{left:338px}.q3{left:576px}
.author{top:942px;display:flex;align-items:center;gap:10px}
.avatar{width:38px;height:38px;border-radius:50%;background:linear-gradient(#7a7f86,#3e434a)}
.author-name{font-family:'Dancing Script',cursive;font-size:15px;color:var(--blue);line-height:16px}
.author-loc{font-size:8px;color:#333;margin-top:2px}
.a1{left:104px}.a2{left:343px}.a3{left:582px}
.dots{left:411px;top:1016px;display:flex;gap:6px}
.dots i{display:block;width:20px;height:2px;background:var(--blue)}
.dots i:nth-child(2){background:var(--green)}

/* footer */
.footer{left:0;top:1037px;width:894px;height:163px;background:var(--footer)}
.social{left:329px;top:1068px;display:flex;gap:7px}
.social i{display:block;width:28px;height:28px;border-radius:50%;background:#fff}
.footer-line{left:98px;top:1112px;width:700px;height:1px;background:#5a5a5a}
.footer-nav{left:0;top:1124px;width:894px;display:flex;justify-content:center;font-size:8.5px;color:#fff}
.footer-nav span{padding:0 14px}
.copy{left:0;top:1155px;width:894px;text-align:center;font-size:8px;color:#fff}
</style>
</head>
<body>
<div class="abs top-line"></div>
<header class="abs header"></header>
<div class="abs brand"><span class="brand-dot"></span><span class="brand-name">Workvana.de</span></div>
<nav class="abs nav">
  <a class="home">HOME</a><a class="about">ABOUT US</a><a class="services">SERVICES</a><a class="contact">CONTACT US</a>
</nav>

<section class="abs hero"></section>
<h1 class="abs hero-title">WORKVANA</h1>
<p class="abs hero-text">Sed ut perspiciatis unde omnis iste natus error sit voluptatem accusantium doloremque laudantium, totam rem aperiam, eaque ipsa quae ab illo &nbsp;totam rem aperiam, eaque ipsa quae inventore veritatis voluptatem sequi ab illo inventore veritatis nesciunt.</p>
<div class="abs cta">LET'S DET STARTED!</div>
<svg class="abs video" viewBox="0 0 367 206" role="img" aria-label="Video placeholder: laptop showing a business video preview with a play button">
  <defs>
    <linearGradient id="videoTone" x1="0" y1="0" x2="1" y2="1">
      <stop offset="0" stop-color="#1f5f9a"/>
      <stop offset=".55" stop-color="#2f8fd0"/>
      <stop offset="1" stop-color="#17456f"/>
    </linearGradient>
  </defs>
  <rect x="0" y="0" width="367" height="206" rx="8" fill="url(#videoTone)"/>
  <circle cx="183" cy="103" r="24" fill="#3a3a3a" fill-opacity=".85"/>
  <path d="M175 90 L196 103 L175 116 Z" fill="var(--green)"/>
</svg>

<section class="abs benefits"></section>
<h2 class="abs section-title benefits-title">OUR 3 <span>BENEFITS</span></h2>
<p class="abs benefits-text">Sed ut perspiciatis unde omnis iste natus error sit voluptatem accusantium doloremque laudantium, totam rem aperiam, eaque ipsa quae ab illo inventore veritatis et quasi architecto beatae vitae dicta sunt explicabo.Nemo enim sed quia consequuntur magni dolores eos qui ratione voluptatem sequi nesciunt.Sed ut perspiciatis unde omnis iste llo inventore veritatis et quasi architecto beatae vitae dicta sunt explicabo.</p>

<div class="abs benefit b1">
  <svg class="benefit-icon" viewBox="0 0 44 42" role="img" aria-label="Growth icon">
    <rect x="4" y="28" width="7" height="12" fill="var(--grey)"/><rect x="14" y="22" width="7" height="18" fill="var(--grey)"/><rect x="24" y="16" width="7" height="24" fill="var(--grey)"/><rect x="34" y="10" width="7" height="30" fill="var(--grey)"/>
    <path d="M4 22 L32 4" stroke="var(--green)" stroke-width="4"/>
  </svg>
  <h3>NEQUE PORRO QUISQUAM</h3>
  <p>Sed ut perspiciatis unde omnis iste natus error sit voluptatem accusan vitae dicta sunt explicabo.</p>
  <div class="more">{ READ MORE }</div>
</div>
<div class="abs benefit b2">
  <svg class="benefit-icon" viewBox="0 0 44 42" role="img" aria-label="Settings icon">
    <circle cx="22" cy="21" r="16" fill="var(--grey)"/><circle cx="22" cy="21" r="6" fill="var(--light)"/>
    <path d="M10 34 L34 10" stroke="var(--green)" stroke-width="5"/>
  </svg>
  <h3>NEQUE PORRO QUISQUAM</h3>
  <p>Sed ut perspiciatis unde omnis iste natus error sit voluptatem accusan vitae dicta sunt explicabo.</p>
  <div class="more">{ READ MORE }</div>
</div>
<div class="abs benefit b3">
  <svg class="benefit-icon" viewBox="0 0 52 42" role="img" aria-label="Team icon">
    <circle cx="15" cy="10" r="8" fill="var(--grey)"/><circle cx="37" cy="10" r="8" fill="var(--grey)"/>
    <path d="M2 32 Q15 14 28 32Z M24 32 Q37 14 50 32Z" fill="var(--grey)"/>
    <circle cx="26" cy="16" r="8" fill="var(--green)"/><path d="M10 40 Q26 18 42 40Z" fill="var(--green)"/>
  </svg>
  <h3>NEQUE PORRO QUISQUAM</h3>
  <p>Sed ut perspiciatis unde omnis iste natus error sit voluptatem accusan vitae dicta sunt explicabo.</p>
  <div class="more">{ READ MORE }</div>
</div>

<form class="abs newsletter">
  <h2>NEWSLETTER</h2>
  <div class="field f1">Enter Your Name :</div>
  <div class="field f2">Enter Your Email :</div>
  <div class="field f3">Enter Your Phone :</div>
  <div class="field f4">Messages :</div>
  <div class="submit">SUBMIT FORM</div>
</form>

<section class="abs testimonials"></section>
<h2 class="abs section-title testi-title">WHAT OUR <span>CUSTOMERS HAVE TO SAY</span></h2>
<blockquote class="abs quote q1">With one snap, these reusable hand warmers, made from a nontoxic salt solution, heat right up. Perfect for pockets and gloves.<span class="close">&#8221;</span></blockquote>
<blockquote class="abs quote q2">With one snap, these reusable hand warmers, made from a nontoxic salt solution, heat right up. Perfect for pockets and gloves.<span class="close">&#8221;</span></blockquote>
<blockquote class="abs quote q3">With one snap, these reusable hand warmers, made from a nontoxic salt solution, heat right up. Perfect for pockets and gloves.<span class="close">&#8221;</span></blockquote>
<div class="abs author a1"><div class="avatar" role="img" aria-label="Customer portrait"></div><div><div class="author-name">Mara Linden</div><div class="author-loc">Location, Area</div></div></div>
<div class="abs author a2"><div class="avatar" role="img" aria-label="Customer portrait"></div><div><div class="author-name">Mara Linden</div><div class="author-loc">Location, Area</div></div></div>
<div class="abs author a3"><div class="avatar" role="img" aria-label="Customer portrait"></div><div><div class="author-name">Mara Linden</div><div class="author-loc">Location, Area</div></div></div>
<div class="abs dots"><i></i><i></i><i></i></div>

<footer class="abs footer"></footer>
<div class="abs social" aria-label="Social links"><i></i><i></i><i></i><i></i><i></i><i></i><i></i></div>
<div class="abs footer-line"></div>
<div class="abs footer-nav"><span>HOME</span><span>/</span><span>ABOUT US</span><span>/</span><span>SERVICES</span><span>/</span><span>CONTACT US</span></div>
<div class="abs copy">© Copy Rights 2014Workvana.All Rights Reserved</div>
</body>
</html>
```